Ecommerce brand for entrepreneurs needs help with branding products

I am looking for help to design a small supplement pouch. Including colours, layout and design.

The business:
The business is called 'Keel Orbit' and our goal is to help entrepreneurs continue to change the world in spite of how difficult it is.

At Keel Orbit, we understand being an entrepreneur is one of the hardest jobs there is. We believe there is a better way. A way in which you don’t have to choose between success in your business and the rest of your life. Our aim is to solve these challenges, so you can stay in the fight a little longer. If we can do this, we can ultimately change the world into a better place.

We will do this through a range of supplements, community, information and physical products to help you optimise their lives.

The product:
The product I am looking to create is for a natural nootropic called

‘The Velvet Compass’

The product will address the challenges with focus and lower attention spans.

So Entrepreneurs can Solve more problems, Help more people and make more money.

Do more in four hours than a whole day. Have Zen like calm. With Zero Jitters & Zero Crashes. Do what others can’t

The design:
I want this to be a small pouch. The final design should be elegant, and minimalist and have an edge that is different.

I have added examples of products that I like below.

I am open to most colour combinations but silver, navy, black, orange, white and translucent are what is taking my fancy right now.

I like the idea of having a translucent package or part of the package like some of the designs below. I also like the matt finish of some of the designs along with the flashes of shininess from silver for contrast. or even using embossing within the packaging.

I have a logo that I have made but I am open to changes on that as well if you see fit. if you do want to do this, I would love to see an emblem next to the words Keel Orbit that encapsulates the brand.

I have done some really really rough mockups myself but would like to see what you have to offer rather than what I have done

The purpose of this image:
I need a 3D mockup of this supplement to be on my landing page to start to take pre-orders.

I am ideally looking for 2 images

1) Supplement packaging on its own
2) Supplement packaging with background coloured lighting, with powder on the ground etc

Need extra days to review

Target Market(s)

The logo: Please also redesign my logo - I would love to see an emblem next to the words Keel Orbit that encapsulates the brand.The business is called 'Keel Orbit' and our goal is to help entrepreneurs continue to change the world in spite of how difficult it is. At Keel Orbit, we understand being an entrepreneur is one of the hardest jobs there is. We believe there is a better way. A way in which you don’t have to choose between success in your business and the rest of your life. Our aim is to solve these challenges, so you can stay in the fight a little longer. If we can do this, we can ultimately change the world into a better place. We will do this through a range of supplements, community, information and physical products to help you optimise their lives.

Industry/Entity Type

Supplements for entrepreneurs

Colors

Requirements
Must have
• The design: I want this to be a small pouch. The final design should be elegant, and minimalist and have an edge that is different. I have added examples of products that I like below. I am open to most colour combinations but silver, navy, black, orange, white and translucent are what is taking my fancy right now. I like the idea of having a translucent package or part of the package like some of the designs below. I also like the matt finish of some of the designs along with the flashes of shininess from silver for contrast. or even using embossing within the packaging.

```html
<!DOCTYPE html>
<html lang="en">
<head>
<meta charset="utf-8">
<title>Keel Orbit — The Velvet Compass pouch</title>
<link href="https://fonts.googleapis.com/css2?family=Mulish:wght@200;300;500;800&display=swap" rel="stylesheet">
<style>
  :root {
    --backdrop: #e9ebe7;
    --pouch-black: #141414;
    --pouch-edge: #0c0c0c;
    --pouch-top: #1b1b1b;
    --seal-line: #262626;
    --brand-orange: #f47b20;
    --ink-white: #ffffff;
    --ink-soft: #cfcfcf;
  }
  * { margin: 0; padding: 0; box-sizing: border-box; }
  html, body {
    width: 1200px;
    height: 800px;
    overflow: hidden;
    background: var(--backdrop);
    font-family: "Mulish", "Helvetica Neue", Arial, sans-serif;
  }
  .canvas {
    position: relative;
    width: 1200px;
    height: 800px;
  }
  .pouch-front {
    position: absolute;
    left: 330px;
    top: 35px;
    width: 540px;
    height: 730px;
    background: linear-gradient(180deg, var(--pouch-top) 0%, var(--pouch-black) 40%, var(--pouch-edge) 100%);
    border-radius: 6px 6px 10px 10px;
    color: var(--ink-white);
    text-align: center;
  }
  .zip-seal {
    position: absolute;
    left: 0;
    right: 0;
    top: 100px;
    height: 2px;
    background: var(--seal-line);
  }
  .brand-name {
    position: absolute;
    top: 245px;
    left: 0;
    right: 0;
    color: var(--brand-orange);
    font-weight: 500;
    font-size: 26px;
    letter-spacing: 6px;
    line-height: 1;
  }
  .product-title {
    position: absolute;
    top: 418px;
    left: 0;
    right: 0;
    line-height: 1;
  }
  .title-light {
    display: block;
    font-weight: 200;
    font-size: 54px;
    letter-spacing: 1px;
  }
  .title-strong {
    display: block;
    font-weight: 500;
    font-size: 54px;
    margin-top: 2px;
  }
  .tagline {
    display: block;
    margin-top: 16px;
    font-weight: 300;
    font-size: 20px;
    color: var(--ink-soft);
    letter-spacing: 0.5px;
    word-spacing: 2px;
  }
  .category {
    position: absolute;
    top: 655px;
    left: 0;
    right: 0;
    font-size: 16px;
    letter-spacing: 4px;
  }
  .category-bold { font-weight: 800; }
  .category-light { font-weight: 300; }
</style>
</head>
<body>
  <main class="canvas">
    <section class="pouch-front">
      <div class="zip-seal"></div>
      <p class="brand-name">KEEL ORBIT</p>
      <h1 class="product-title">
        <span class="title-light">THE VELVET</span>
        <span class="title-strong">COMPASS</span>
        <span class="tagline">ZERO JITTERS &amp; ZERO CRASHES</span>
      </h1>
      <p class="category"><span class="category-bold">NATURAL</span> <span class="category-light">NOOTROPIC</span></p>
    </section>
  </main>
</body>
</html>
```